New Business Card Design Project

Use the flyer uploaded and website www.brightoakbuilders.com for inspiration.
List Our Services on Backside of business cards
Martin Hollis
Harborline Renovations Inc.
Licensed General Contractors
858-471-9063

Contact Information for Business Card

Use the flyer uploaded and website www.brightoakbuilders.com for inspiration. List Our Services on Backside of business cards Martin Hollis Harborline Renovations Inc. Licensed General Contractors 858-471-9063

```html
<!DOCTYPE html>
<html lang="en">
<head>
<meta charset="utf-8">
<title>Harborline Renovations Business Cards</title>
<link rel="stylesheet" href="https://fonts.googleapis.com/css2?family=Anton&family=Poppins:wght@400;500;600&display=swap">
<style>
  :root {
    --blue: #0d47f5;
    --ink: #121314;
    --white: #ffffff;
    --page: #ffffff;
  }
  * { box-sizing: border-box; margin: 0; padding: 0; }
  html, body { width: 1199px; height: 1200px; overflow: hidden; background: var(--page); }
  .canvas { position: relative; width: 1199px; height: 1200px; }

  .card {
    position: absolute; left: 250px; width: 700px; height: 400px;
    overflow: hidden; font-family: "Poppins", sans-serif; color: var(--white);
    box-shadow: 0 6px 18px rgba(0,0,0,0.12);
  }
  .card--back { top: 150px; background: var(--blue); }
  .card--front { top: 650px; background: var(--ink); }

  /* framed panel built from stacked stripes */
  .frame { position: absolute; }
  .frame__stripe { position: absolute; inset: 0; }

  .card--back .frame { left: 0; top: 86px; right: 14px; bottom: 0; }
  .card--back .s1 { background: var(--white); }
  .card--back .s2 { inset: 6px 6px 0 0; background: var(--ink); }
  .card--back .s3 { inset: 12px 12px 0 0; background: var(--blue); }
  .card--back .s4 { inset: 18px 18px 0 0; background: var(--ink); }

  .card--front .frame { left: 300px; top: 150px; right: 0; bottom: 0; }
  .card--front .s1 { background: var(--blue); }
  .card--front .s2 { inset: 6px 0 0 6px; background: var(--ink); }
  .card--front .s3 { inset: 12px 0 0 12px; background: var(--white); }
  .card--front .s4 { inset: 18px 0 0 18px; background: var(--blue); }

  .brand {
    position: absolute; display: flex; align-items: center; gap: 12px;
    font-weight: 400; font-size: 24px; letter-spacing: 2px; text-transform: uppercase;
    color: var(--white);
  }
  .brand__mark { width: 14px; height: 14px; background: var(--white); }
  .card--back .brand { left: 170px; top: 180px; }
  .card--front .brand { left: 50px; top: 120px; }

  .website {
    position: absolute; left: 170px; top: 250px;
    font-size: 22px; font-weight: 500; letter-spacing: 4px;
  }

  .contact { position: absolute; left: 350px; top: 200px; }
  .contact__name {
    font-family: "Anton", sans-serif; font-size: 46px; line-height: 1;
    letter-spacing: 1px; text-transform: uppercase; margin-bottom: 10px;
  }
  .contact__line { font-size: 16px; font-weight: 500; line-height: 1.3; }
  .contact__phone { display: flex; align-items: center; gap: 8px; margin-top: 2px; }
  .contact__phone svg { width: 14px; height: 14px; }
</style>
</head>
<body>
<main class="canvas">

  <section class="card card--back" aria-label="Card back">
    <div class="frame">
      <div class="frame__stripe s1"></div>
      <div class="frame__stripe s2"></div>
      <div class="frame__stripe s3"></div>
      <div class="frame__stripe s4"></div>
    </div>
    <div class="brand"><span class="brand__mark"></span>Harborline Renovations</div>
    <p class="website">www.brightoakbuilders.com</p>
  </section>

  <section class="card card--front" aria-label="Card front">
    <div class="brand"><span class="brand__mark"></span>Harborline Renovations</div>
    <div class="frame">
      <div class="frame__stripe s1"></div>
      <div class="frame__stripe s2"></div>
      <div class="frame__stripe s3"></div>
      <div class="frame__stripe s4"></div>
    </div>
    <div class="contact">
      <h1 class="contact__name">Martin Hollis</h1>
      <p class="contact__line">Harborline Renovations Inc.</p>
      <p class="contact__line">Licensed General<br>Contractors</p>
      <p class="contact__line contact__phone">
        <svg viewBox="0 0 24 24" aria-hidden="true"><path fill="#ffffff" d="M6.6 10.8a15.1 15.1 0 0 0 6.6 6.6l2.2-2.2a1 1 0 0 1 1-.25 11.4 11.4 0 0 0 3.6.57 1 1 0 0 1 1 1V20a1 1 0 0 1-1 1A17 17 0 0 1 3 4a1 1 0 0 1 1-1h3.5a1 1 0 0 1 1 1c0 1.25.2 2.45.57 3.57a1 1 0 0 1-.25 1z"/></svg>
        858-471-9063
      </p>
    </div>
  </section>

</main>
</body>
</html>
```